"The Craft of Patron Care," fourth edition cover design

Later this year, my publisher, Harold Brenton & Co., will issue a fourth, substantially revised edition of "The Craft of Patron Care," following the 2016 publication of the third edition and the second and first versions that were issued earlier.

To distinguish this new edition from previous ones, I need a cover design that visually connects and is consistent with what has preceded it, while signaling this is a new and different, worthy of prospective readers/buyers’ attention.

Attached are three different verbal approaches to the new cover; these are NOT MEANT to serve as actual designs, but rather will give you a sense of how language is to be deployed:

The first emphasizes “ART” as the key visual word in the book title;
The second emphasizes “CLIENT SERVICE” as the key visual words in the book title; and,
The third emphasizes just the word "CLIENT" in the book title.

A top-of-the-page is a pre-head that applies to all three versions:
“6 TIMELESS PRINCIPLES FOR ADVERTISING & MARKETING PRO’s
IN AN AI WORLD"

There's a mid-page sub-head for all three versions:
“THE CLASSIC GUIDE,” followed by
“FOURTH EDITION BY DENNIS HARTWELL

And there's a one-line, bottom-of-the-page designation:
“Foreword by Pam Kettering, Global Executive Creative Director, Bluefinch"

The pallette for the previously published third edition was black with red as an accent color on a field of white; I've attached a sample for reference, so you can see how it was executed. For this new fourth edition, I'd like to change the accent color from red to either Wedgewood blue, or British racing green, or an alternative that is assertive and color saturated -- think of primary colors -- that contrast sufficiently with the base of black. As an alternative, you can consider a cover that used either Wedgewood blue, British racing green, or another possibility as a full-bleed field, with copy content either revered out or surprinted.

Lastly, while the new cover largely is meant to be typographically driven, if you can come up with a visual metaphor that illustrates and builds on the book's title, that would be very helpful. By way of reference, the third edition's book cover attempted to do this by introducing a visual element at the end of the book's title that's meant to represent an artist's paint splatter (although I admit it didn't work as well as it should).

Target Market(s)

Prospective purchasers of the book who might discover copies at a bookstore, but more likely will encounter it through online distributors such as Vendora, Fitch & Marlow, and Tindle’s.

Industry/Entity Type

Advertising and marketing

Font styles to use
Serif
Sans Serif
Other font styles liked:
• A mix of serif and san-serif typefaces is okay. for the examples I shared, I relieid on "Arial Rounded Bold" but you need not be weeded to this. If you opt to mix in a serif font, I am partial to Cambria as a typeface.

Requirements
Must have
• To achieve the goal of being “connected with but distinct” from previous editions, the new cover should be:  Largely typographic, but displaying a color palette different from the previous editions’ black-plus-red-accent on a canvas of white.  Any new accent color selected for use should be vibrant, strong, and highly saturated; think “British racing green,” “Wedgewood blue,” or their equivalents.  In addition to a powerful, “billboard” approach to type and color, consider other visual metaphors that are likely to engage the readers. The winning cover design will stand out from other books, while connecting with the previously published third edition.
Nice to have
• If you can find way to illustrate the book's title through a visual metaphor, that would be ideal.a
Should not have
• Anything that is frivolous or non-sensical

```html
<!DOCTYPE html>
<html lang="en">
<head>
<meta charset="utf-8">
<title>The Craft of Patron Care — Fourth Edition Cover</title>
<link rel="stylesheet" href="https://fonts.googleapis.com/css2?family=Noto+Serif:ital,wght@0,700;0,800;1,700;1,800&family=Poppins:wght@400;500;600;700&display=swap">
<style>
  :root {
    --paper: #ffffff;
    --ink: #000000;
    --racing-green: #02432a;
    --serif: "Noto Serif", Georgia, serif;
    --sans: "Poppins", Arial, sans-serif;
  }
  html, body {
    margin: 0;
    padding: 0;
    overflow: hidden;
    background: var(--paper);
  }
  .cover {
    position: relative;
    width: 752px;
    height: 1200px;
    background: var(--paper);
    color: var(--ink);
    overflow: hidden;
  }
  .prehead {
    position: absolute;
    top: 76px;
    left: 0;
    width: 100%;
    margin: 0;
    text-align: center;
    font-family: var(--sans);
    font-weight: 400;
    font-size: 20.5px;
    line-height: 31px;
    letter-spacing: 0.2px;
  }
  .prehead .accent {
    color: var(--racing-green);
    font-weight: 600;
  }
  .title {
    position: absolute;
    inset: 0;
    margin: 0;
    font-family: var(--serif);
    font-weight: 800;
  }
  .title > span {
    position: absolute;
    display: block;
    line-height: 1;
    white-space: nowrap;
  }
  .title-the {
    left: 80px;
    top: 342px;
    font-style: italic;
    font-size: 71px;
    letter-spacing: -1px;
  }
  .title-key {
    left: 206px;
    top: 387px;
    font-size: 116px;
    color: var(--racing-green);
    letter-spacing: -3px;
  }
  .title-of {
    left: 604px;
    top: 424px;
    font-size: 74px;
  }
  .title-bottom {
    left: 0;
    top: 514px;
    width: 100%;
    text-align: center;
    font-size: 98px;
    letter-spacing: -1px;
  }
  .divider {
    position: absolute;
    top: 686px;
    left: 75px;
    width: 603px;
    height: 2px;
    background: var(--ink);
    border: 0;
    margin: 0;
  }
  .series {
    position: absolute;
    top: 758px;
    left: 0;
    width: 100%;
    margin: 0;
    text-align: center;
    font-family: var(--sans);
    font-weight: 600;
    font-size: 51px;
    line-height: 1.1;
    letter-spacing: 0.5px;
  }
  .edition {
    position: absolute;
    top: 826px;
    left: 0;
    width: 100%;
    margin: 0;
    text-align: center;
    font-family: var(--sans);
    font-weight: 700;
    font-size: 31px;
    line-height: 1.2;
  }
  .edition .accent {
    color: var(--racing-green);
  }
  .byline {
    position: absolute;
    top: 1016px;
    left: 0;
    width: 100%;
    margin: 0;
    text-align: center;
    font-family: var(--sans);
    font-weight: 700;
    font-size: 17px;
  }
  .author {
    position: absolute;
    top: 1052px;
    left: 0;
    width: 100%;
    margin: 0;
    text-align: center;
    font-family: var(--serif);
    font-weight: 700;
    font-size: 29px;
    color: var(--racing-green);
    letter-spacing: 0.3px;
  }
  .foreword {
    position: absolute;
    top: 1105px;
    left: 0;
    width: 100%;
    margin: 0;
    text-align: center;
    font-family: var(--sans);
    font-weight: 500;
    font-size: 16px;
  }
</style>
</head>
<body>
<main class="cover">
  <p class="prehead">6 TIMELESS PRINCIPLES FOR ADVERTISING &amp; MARKETING<br>PRO’s IN AN <span class="accent">AI WORLD</span></p>

  <h1 class="title">
    <span class="title-the">The</span>
    <span class="title-key">CRAFT</span>
    <span class="title-of">Of</span>
    <span class="title-bottom">Patron Care</span>
  </h1>

  <hr class="divider">

  <p class="series">THE CLASSIC GUIDE</p>
  <p class="edition"><span class="accent">FOURTH</span> EDITION</p>

  <p class="byline">By</p>
  <p class="author">DENNIS HARTWELL</p>
  <p class="foreword">Foreword by Pam Kettering, Global Executive Creative Director, Bluefinch</p>
</main>
</body>
</html>
```